Business Card Design Project

We need a double-sided business card design for our e-commerce company. Be as creative as you can.

Reason: Change of logo

Target Market(s)

Business owners

Industry/Entity Type

E-Commerce

Requirements
Must have
• Name (editable)
Mobile number -editable
www.velbiro.com - MUST STAND OUT ALONE
Office address:
27 Marlow Street
#09-04 Westbrook Tower
Singapore 048216

```html
<!DOCTYPE html>
<html lang="en">
<head>
<meta charset="utf-8">
<title>Velbiro Business Card</title>
<link rel="stylesheet" href="https://fonts.googleapis.com/css2?family=Encode+Sans+Condensed:wght@400&family=Montserrat:wght@500;600&display=swap">
<style>
  :root {
    --backdrop: #4a2e16;
    --card-black: #000000;
    --facet-dark: #111111;
    --facet-mid: #3c3c3c;
    --facet-light: #9a9a9a;
    --brand-orange: #f47a20;
    --text-orange: #f7941d;
    --url-red: #e8202a;
  }
  html, body {
    margin: 0;
    padding: 0;
    width: 1200px;
    height: 1200px;
    overflow: hidden;
    background: var(--backdrop);
  }
  .canvas {
    position: relative;
    width: 1200px;
    height: 1200px;
  }
  .card {
    position: absolute;
    left: 132px;
    width: 888px;
    background: var(--card-black);
  }
  .card-front {
    top: 86px;
    height: 514px;
    overflow: hidden;
  }
  .facet-pattern {
    position: absolute;
    inset: 0;
    background:
      repeating-linear-gradient(90deg, var(--facet-dark) 0 60px, var(--facet-mid) 90px, var(--facet-light) 120px, var(--facet-dark) 121px 150px),
      var(--facet-dark);
    opacity: 0.9;
  }
  .brand-name {
    position: absolute;
    left: 0;
    right: 0;
    top: 206px;
    margin: 0;
    text-align: center;
    font-family: "Montserrat", sans-serif;
    font-weight: 600;
    font-size: 150px;
    line-height: 1;
    letter-spacing: -2px;
    color: var(--brand-orange);
  }
  .card-back {
    top: 622px;
    height: 512px;
  }
  .contact-name,
  .contact-mobile {
    position: absolute;
    left: 62px;
    margin: 0;
    font-family: "Encode Sans Condensed", sans-serif;
    color: var(--text-orange);
    line-height: 1;
  }
  .contact-name { top: 96px; font-size: 44px; }
  .contact-mobile { top: 152px; font-size: 35px; }
  .website {
    position: absolute;
    left: 62px;
    top: 198px;
    margin: 0;
    font-family: "Montserrat", sans-serif;
    font-weight: 500;
    font-size: 52px;
    line-height: 1;
    letter-spacing: 1px;
    color: var(--url-red);
  }
  .office-address {
    position: absolute;
    left: 404px;
    top: 278px;
    margin: 0;
    font-style: normal;
    color: var(--text-orange);
  }
  .office-address span {
    display: block;
    font-family: "Montserrat", sans-serif;
    font-weight: 500;
    font-size: 34px;
    line-height: 40px;
    letter-spacing: 2px;
  }
  .office-address .address-unit {
    font-family: "Encode Sans Condensed", sans-serif;
    font-weight: 400;
    font-size: 38px;
    letter-spacing: 0;
  }
</style>
</head>
<body>
  <main class="canvas">
    <section class="card card-front">
      <div class="facet-pattern" role="img" aria-label="Black and silver faceted triangle pattern"></div>
      <h1 class="brand-name">velbiro</h1>
    </section>
    <section class="card card-back">
      <p class="contact-name">Name</p>
      <p class="contact-mobile">Mobile No</p>
      <p class="website">www.velbiro.com</p>
      <address class="office-address">
        <span>Office address:</span>
        <span>27 Marlow Street</span>
        <span class="address-unit">No:09-04 Westbrook Tower</span>
        <span>Singapore 048216</span>
      </address>
    </section>
  </main>
</body>
</html>
```